Lom Consulting -New consulting business in architecture, urban planning, and real estate development

We need a stationery design, including logo, business cards, etc, work for a new consulting business that works in the world of architectural, urban planning and real estate development.

The name of the company is "Lom Consulting". Lom is my last name but it of course also has the meaning 'cool' and 'hip'.

Target Market(s)

The business will provide boutique consulting services to high end clients that may include property developers, cities, etc.

Industry/Entity Type

Consultant

Contact Information for Business Card

LOM Consulting
First Name Last Name
Title
Phone number
Address
Website
Optional: Twitter handle

Logo Text

LOM Consulting

Font styles to use
Sans Serif

Colors

Designer to choose colors to be used in the design.

Requirements
Must have
• Simple design
• Easy to read font
• Modern
• Elegance
• Nice font that can be used for future reports, letters, etc.
• Good colour scheme that allows for the elegance to come through
Should not have
• Complex design ideas
• Complex logos
• Not a corporate feel and look

```html
<!DOCTYPE html>
<html lang="en">
<head>
<meta charset="utf-8">
<title>LOM Consulting – Business Card</title>
<link href="https://fonts.googleapis.com/css2?family=Jost:wght@400;500;600&display=swap" rel="stylesheet">
<style>
  :root {
    --backdrop: #2e2e30;
    --card-dark: #353536;
    --card-light: #f1f1f1;
    --gold: #c9a23c;
    --ink: #333333;
    --ink-soft: #4a4a4a;
    --rule: #c8c8c8;
  }
  * { margin: 0; padding: 0; box-sizing: border-box; }
  html, body {
    width: 1200px; height: 1123px; overflow: hidden;
    background: var(--backdrop);
    font-family: "Jost", sans-serif;
  }
  .canvas { position: relative; width: 1200px; height: 1123px; }

  .card {
    position: absolute; left: 312px; width: 590px; height: 337px;
    border-radius: 18px;
  }
  .card--front { top: 182px; background: var(--card-dark); }
  .card--back  { top: 604px; background: var(--card-light); }

  .brand {
    position: absolute; color: var(--gold);
    font-family: "Jost", sans-serif; font-weight: 500;
    text-align: center; line-height: 1;
  }
  .brand__name { display: block; letter-spacing: 0.04em; }
  .brand__sub  { display: block; letter-spacing: 0.38em; margin-right: -0.38em; }

  .card--front .brand { left: 0; right: 0; top: 96px; }
  .card--front .brand__name { font-size: 118px; }
  .card--front .brand__sub  { font-size: 21px; margin-top: 18px; }

  .card--back .brand { left: 76px; width: 190px; top: 116px; }
  .card--back .brand__name { font-size: 92px; }
  .card--back .brand__sub  { font-size: 16px; margin-top: 14px; }

  .divider {
    position: absolute; left: 290px; top: 90px;
    width: 1px; height: 171px; background: var(--rule);
  }

  .contact { position: absolute; left: 332px; top: 88px; color: var(--ink-soft); }
  .contact__name {
    font-size: 24px; font-weight: 600; color: var(--ink);
    line-height: 1; letter-spacing: 0.01em;
  }
  .contact__title { font-size: 14px; margin-top: 4px; }
  .contact__address { font-size: 14px; line-height: 19px; margin-top: 11px; }
  .contact__list { list-style: none; margin-top: 10px; }
  .contact__item {
    display: flex; align-items: center; gap: 8px;
    font-size: 14px; line-height: 18.5px;
  }
  .contact__icon { width: 14px; height: 14px; flex: none; }
</style>
</head>
<body>
<main class="canvas">

  <section class="card card--front" aria-label="Card front">
    <div class="brand">
      <span class="brand__name">LOM</span>
      <span class="brand__sub">CONSULTING</span>
    </div>
  </section>

  <section class="card card--back" aria-label="Card back">
    <div class="brand">
      <span class="brand__name">LOM</span>
      <span class="brand__sub">CONSULTING</span>
    </div>

    <div class="divider"></div>

    <div class="contact">
      <p class="contact__name">Daniel HARPER</p>
      <p class="contact__title">Managing Director</p>
      <p class="contact__address">412 N Maple Avenue<br>Linden, MS 39150</p>
      <ul class="contact__list">
        <li class="contact__item">
          <svg class="contact__icon" viewBox="0 0 16 16" aria-hidden="true"><path d="M3 1.5l3 .5 1 3-2 1.5c1 2 2.5 3.5 4.5 4.5L11 9l3 1 .5 3-2 1.5C7 14 2 9 1.5 3.5z" fill="var(--gold)"/></svg>
          <span>000.000.0000</span>
        </li>
        <li class="contact__item">
          <svg class="contact__icon" viewBox="0 0 16 16" aria-hidden="true"><rect x="4.5" y="1.5" width="7" height="13" rx="1.2" fill="none" stroke="var(--gold)" stroke-width="1.4"/><circle cx="8" cy="12.2" r="0.9" fill="var(--gold)"/></svg>
          <span>000.000.0000</span>
        </li>
        <li class="contact__item">
          <svg class="contact__icon" viewBox="0 0 16 16" aria-hidden="true"><rect x="1.5" y="3.5" width="13" height="9" fill="none" stroke="var(--gold)" stroke-width="1.2"/><path d="M1.5 3.5L8 9l6.5-5.5M1.5 12.5L6 8M14.5 12.5L10 8" fill="none" stroke="var(--gold)" stroke-width="1.1"/></svg>
          <span>daniel@lomconsulting.com</span>
        </li>
        <li class="contact__item">
          <svg class="contact__icon" viewBox="0 0 16 16" aria-hidden="true"><g fill="none" stroke="var(--gold)" stroke-width="1.1"><circle cx="8" cy="8" r="6.5"/><ellipse cx="8" cy="8" rx="3" ry="6.5"/><path d="M1.5 8h13M2.5 4.8h11M2.5 11.2h11"/></g></svg>
          <span>www.lomconsulting.com</span>
        </li>
      </ul>
    </div>
  </section>

</main>
</body>
</html>
```